Birchford Realty Business Card

Business Card:

Somewhere on front of card, please include Broker License Number: 5839162

Website is BirchfordRealty.example

Address is:
7218 Crestover Ave E
Saginaw, MI 48271

I'll let you use creative freedom on the rest; we obviously need Name, Title, Email (@BirchfordRealty.example), Office Phone, Cell Phone.

Don't want any special die-cutting, just a standard size business card.

On the back, include a place for the date and time of an appointment to be written in pen.

Requirements
Must have
• Our logo, attached to email.

```html
<!DOCTYPE html>
<html lang="en">
<head>
<meta charset="utf-8">
<title>Birchford Realty Business Card</title>
<link rel="stylesheet" href="https://fonts.googleapis.com/css2?family=Open+Sans:wght@400;600;700&family=Crimson+Text:wght@400;600&display=swap">
<style>
  :root {
    --canvas: #ececec;
    --card: #ffffff;
    --orange: #e2801c;
    --red: #e8202b;
    --charcoal: #2f2f34;
    --steel: #5a5a60;
    --mist: #cfcfd3;
    --navy: #232a6e;
    --link-blue: #1a1ad8;
    --ink: #111111;
    --watermark: rgba(35, 42, 110, 0.12);
  }
  * { box-sizing: border-box; margin: 0; padding: 0; }
  html, body { width: 1200px; height: 784px; overflow: hidden; }
  body { background: var(--canvas); position: relative; font-family: "Open Sans", Arial, sans-serif; }

  .card {
    position: absolute;
    top: 244px;
    width: 520px;
    height: 297px;
    background: var(--card);
    overflow: hidden;
    box-shadow: 0 6px 18px rgba(0,0,0,0.18);
  }
  .card-back { left: 60px; }
  .card-front { left: 620px; }
  .card-art { position: absolute; inset: 0; width: 100%; height: 100%; }

  /* Front */
  .license {
    position: absolute; top: 16px; right: 18px;
    color: var(--link-blue); font-size: 14px;
  }
  .license .license-no { font-size: 11px; }
  .brand-name {
    position: absolute; top: 118px; left: 196px;
    color: var(--navy); font-weight: 700; font-size: 30px; letter-spacing: -0.5px;
  }
  .address {
    position: absolute; top: 176px; left: 262px;
    color: var(--ink); font-size: 16px; line-height: 1.3;
  }
  .website {
    position: absolute; bottom: 16px; right: 20px;
    color: var(--link-blue); font-size: 14px;
  }

  /* Back */
  .watermark {
    position: absolute; top: 104px; left: 120px;
    color: var(--watermark); font-weight: 700; font-size: 56px;
    letter-spacing: -1px; white-space: nowrap;
  }
  .appointment {
    position: absolute; inset: 0;
    font-family: "Crimson Text", Georgia, serif; color: var(--ink);
  }
  .appointment-title {
    position: absolute; top: 14px; left: 216px;
    font-size: 24px; font-weight: 600;
  }
  .fields { position: absolute; top: 66px; left: 28px; right: 28px; }
  .field-row { display: flex; gap: 14px; margin-bottom: 9px; }
  .field { display: flex; align-items: flex-end; flex: 1; font-size: 17px; }
  .field-line { flex: 1; border-bottom: 2px dotted var(--ink); margin-left: 6px; height: 16px; }
  .days {
    position: absolute; left: 130px; right: 24px; bottom: 16px;
    display: flex; justify-content: space-between;
  }
  .day { display: flex; flex-direction: column; align-items: center; font-size: 12px; }
  .day-box { width: 22px; height: 22px; border: 2px solid var(--ink); margin-top: 3px; background: var(--card); }
</style>
</head>
<body>

<section class="card card-back" aria-label="Card back: appointment reminder">
  <svg class="card-art" viewBox="0 0 520 297" preserveAspectRatio="none" aria-hidden="true">
    <defs>
      <linearGradient id="back-sweep" x1="0" y1="0" x2="1" y2="0">
        <stop offset="0" stop-color="var(--orange)"/>
        <stop offset="1" stop-color="var(--red)"/>
      </linearGradient>
    </defs>
    <path d="M190,0 C310,14 430,52 520,112 L520,0 Z" fill="url(#back-sweep)"/>
    <path d="M0,170 C40,220 80,262 128,297 L0,297 Z" fill="var(--charcoal)"/>
    <path d="M0,150 C26,186 52,214 82,240 C50,226 22,204 0,184 Z" fill="var(--mist)"/>
  </svg>
  <div class="watermark">Birchford Realty</div>
  <div class="appointment">
    <h2 class="appointment-title">Appointment</h2>
    <div class="fields">
      <div class="field-row"><div class="field">Name<span class="field-line"></span></div></div>
      <div class="field-row"><div class="field">Title<span class="field-line"></span></div></div>
      <div class="field-row"><div class="field">E-mail<span class="field-line"></span></div></div>
      <div class="field-row">
        <div class="field">Office-No<span class="field-line"></span></div>
        <div class="field">Mobile-No<span class="field-line"></span></div>
      </div>
      <div class="field-row">
        <div class="field">Date<span class="field-line"></span></div>
        <div class="field">Time<span class="field-line"></span></div>
      </div>
    </div>
    <div class="days">
      <div class="day">Monday<span class="day-box"></span></div>
      <div class="day">Tuesday<span class="day-box"></span></div>
      <div class="day">Wednesday<span class="day-box"></span></div>
      <div class="day">Thursday<span class="day-box"></span></div>
      <div class="day">Friday<span class="day-box"></span></div>
      <div class="day">Saturday<span class="day-box"></span></div>
      <div class="day">Sunday<span class="day-box"></span></div>
    </div>
  </div>
</section>

<section class="card card-front" aria-label="Card front">
  <svg class="card-art" viewBox="0 0 520 297" preserveAspectRatio="none" aria-hidden="true">
    <defs>
      <linearGradient id="front-sweep" x1="0" y1="0" x2="1" y2="0">
        <stop offset="0" stop-color="var(--orange)"/>
        <stop offset="1" stop-color="var(--red)"/>
      </linearGradient>
      <linearGradient id="front-dark" x1="0" y1="1" x2="1" y2="0">
        <stop offset="0" stop-color="var(--charcoal)"/>
        <stop offset="1" stop-color="var(--steel)"/>
      </linearGradient>
    </defs>
    <path d="M60,297 C90,150 160,40 300,0 L520,0 L520,297 Z" fill="url(#front-sweep)"/>
    <path d="M100,297 C130,190 200,100 320,62 L520,62 L520,297 Z" fill="url(#front-dark)"/>
    <ellipse cx="362" cy="252" rx="252" ry="196" fill="var(--mist)"/>
    <ellipse cx="382" cy="258" rx="240" ry="190" fill="var(--card)"/>
  </svg>
  <p class="license">License Number: <span class="license-no">5839162</span></p>
  <p class="brand-name">Birchford Realty</p>
  <p class="address">7218 Crestover Ave E<br>Saginaw, MI 48271</p>
  <p class="website">www.BirchfordRealty.example</p>
</section>

</body>
</html>
```